Ombrik Partnering Business Card

Hello everyone. We need a business card design that would match our logo and the theme we're trying to have for Ombrik that you can find on our website and/or Linkedin page

```html
<!DOCTYPE html>
<html lang="en">
<head>
<meta charset="utf-8">
<title>Ombrik Partnering Business Card</title>
<link href="https://fonts.googleapis.com/css2?family=Roboto:wght@400;500&family=Roboto+Condensed:wght@400;700&display=swap" rel="stylesheet">
<style>
  :root {
    --backdrop: #2a2a2c;
    --card-front: #f7f7f5;
    --card-back: #1e1e20;
    --brand-purple: #3d1d6e;
    --accent-purple: #4b2a8a;
    --text-light: #f2f2f2;
    --text-muted: #b9b9b9;
    --text-web: #555555;
    --divider: #8a8a8a;
  }
  * { margin: 0; padding: 0; box-sizing: border-box; }
  html, body { width: 1200px; height: 900px; overflow: hidden; }
  body {
    background: var(--backdrop);
    font-family: "Roboto", Arial, sans-serif;
    position: relative;
  }
  .card {
    position: absolute;
    left: 285px;
    width: 630px;
    height: 360px;
    border-radius: 3px;
    box-shadow: 0 10px 24px rgba(0,0,0,0.45);
  }
  .card--front { top: 70px; background: var(--card-front); }
  .card--back { top: 470px; background: var(--card-back); }

  .brand {
    position: absolute;
    top: 120px; left: 0; right: 0;
    display: flex; justify-content: center; align-items: center; gap: 14px;
  }
  .brand__dot {
    width: 22px; height: 22px; border-radius: 50%;
    background: var(--brand-purple);
  }
  .brand__name {
    font-family: "Roboto", Arial, sans-serif;
    font-weight: 500;
    font-size: 40px;
    color: var(--brand-purple);
    letter-spacing: 0.5px;
  }
  .front__web {
    position: absolute;
    bottom: 62px; left: 0; right: 0;
    text-align: center;
    font-size: 15px;
    letter-spacing: 7px;
    color: var(--text-web);
  }

  .person {
    position: absolute;
    top: 118px; right: 372px;
    text-align: right;
    font-family: "Roboto Condensed", Arial, sans-serif;
  }
  .person__name {
    font-weight: 700;
    font-size: 34px;
    color: var(--accent-purple);
    line-height: 1;
  }
  .person__title {
    font-size: 17px;
    color: var(--text-muted);
    margin-top: 6px;
  }
  .divider {
    position: absolute;
    top: 98px; left: 280px;
    width: 1px; height: 112px;
    background: var(--divider);
  }
  .contacts {
    position: absolute;
    top: 106px; left: 304px;
    list-style: none;
  }
  .contacts li {
    display: flex; align-items: center; gap: 10px;
    font-size: 16px; color: var(--text-light);
    line-height: 24px;
  }
  .icon { width: 14px; height: 14px; fill: var(--accent-purple); flex: none; }
  .address {
    position: absolute;
    bottom: 58px; left: 82px;
    display: flex; align-items: center; gap: 6px;
    font-size: 18px; color: var(--text-light);
  }
  .address .icon { width: 16px; height: 18px; }
</style>
</head>
<body>
  <section class="card card--front">
    <div class="brand">
      <span class="brand__dot"></span>
      <span class="brand__name">Ombrik Partnering</span>
    </div>
    <p class="front__web">www.ombrikpartnering.com</p>
  </section>

  <section class="card card--back">
    <div class="person">
      <p class="person__name">DANA KELLER</p>
      <p class="person__title">CEO/FOUNDER</p>
    </div>
    <div class="divider"></div>
    <ul class="contacts">
      <li>
        <svg class="icon" viewBox="0 0 16 16" aria-hidden="true"><path d="M3.5 1l3 3-1.6 2.2a9 9 0 0 0 4.9 4.9L12 9.5l3 3-2 2.5C6.5 15 1 9.5 1 3z"/></svg>
        555 210 4831
      </li>
      <li>
        <svg class="icon" viewBox="0 0 16 16" aria-hidden="true"><path d="M4 0h8a1 1 0 0 1 1 1v14a1 1 0 0 1-1 1H4a1 1 0 0 1-1-1V1a1 1 0 0 1 1-1zm1 2v10h6V2zm3 11a1 1 0 1 0 0 2 1 1 0 0 0 0-2z"/></svg>
        555 378 1926
      </li>
      <li>
        <svg class="icon" viewBox="0 0 16 16" aria-hidden="true"><path d="M1 3h14v1.2L8 9 1 4.2zm0 2.6l7 4.8 7-4.8V13H1z"/></svg>
        dana@ombrikpartnering.com
      </li>
      <li>
        <svg class="icon" viewBox="0 0 16 16" aria-hidden="true"><circle cx="8" cy="8" r="7"/></svg>
        www.ombrikpartnering.com
      </li>
    </ul>
    <p class="address">
      <svg class="icon" viewBox="0 0 16 18" aria-hidden="true"><path d="M8 0a6 6 0 0 1 6 6c0 4.5-6 12-6 12S2 10.5 2 6a6 6 0 0 1 6-6zm0 3.5a2.5 2.5 0 1 0 0 5 2.5 2.5 0 0 0 0-5z"/></svg>
      2140 Larkspur Court, Anchorage, Alaska 99508
    </p>
  </section>
</body>
</html>
```